COMPANY SIGN

I am in the process of ordering new company For Sale signs and stationary (business cards, envelopes, letterheads, and labels). I need a new design with my existing company logo. The TWO MOST IMPORTANT PROJECTS I need right now is the new design for the company sign and business cards. I've uploaded a .jpg file of my company logo.

I like the design to be eye catching and the background color of the company sign to be soothing to the eyes. Perhaps, using one of the color on the leaves of the logo or any other color that the designer think will go well with the logo. My favorite colors are teal or light olive color but don't let that affect your creativity.

Industry/Entity Type

Business

Requirements
Should not have
• Please don't use "Times New Roman" fonts or fonts that is hard to read.

```html
<!DOCTYPE html>
<html lang="en">
<head>
<meta charset="utf-8">
<title>For Sale Signs</title>
<link rel="stylesheet" href="https://fonts.googleapis.com/css2?family=Arimo:wght@700&display=swap">
<style>
  :root {
    --navy: #031e5a;
    --white: #ffffff;
    --edge-dark: #0b0b1a;
    --page: #ffffff;
  }
  html, body {
    margin: 0;
    padding: 0;
    width: 1200px;
    height: 588px;
    overflow: hidden;
    background: var(--page);
  }
  .canvas {
    position: relative;
    width: 1200px;
    height: 588px;
    font-family: "Arimo", Arial, Helvetica, sans-serif;
    font-weight: 700;
  }
  .sign {
    position: absolute;
    top: 47px;
    width: 493px;
    height: 493px;
    border-radius: 12px;
    box-sizing: border-box;
  }
  .sign--navy {
    left: 82px;
    background: var(--navy);
    border: 2px solid var(--edge-dark);
    color: var(--white);
  }
  .sign--white {
    left: 630px;
    background: var(--white);
    border: 2px solid var(--navy);
    color: var(--navy);
  }
  .sign__line {
    position: absolute;
    left: 0;
    right: 0;
    margin: 0;
    text-align: center;
    font-size: 160px;
    line-height: 160px;
    letter-spacing: -2px;
  }
  .sign__line--top { top: 39px; }
  .sign__line--bottom { top: 183px; }
  .brand {
    position: absolute;
    left: 0;
    right: 0;
    top: 372px;
    display: flex;
    flex-direction: column;
    align-items: center;
    gap: 10px;
  }
  .brand__mark {
    width: 24px;
    height: 24px;
    border-radius: 50%;
    background: currentColor;
  }
  .brand__name {
    font-size: 20px;
    line-height: 24px;
    letter-spacing: 0.5px;
    text-align: center;
  }
</style>
</head>
<body>
<main class="canvas">
  <section class="sign sign--navy">
    <p class="sign__line sign__line--top">FOR</p>
    <p class="sign__line sign__line--bottom">SALE</p>
    <div class="brand">
      <span class="brand__mark"></span>
      <span class="brand__name">Maple Lane<br>Home Tour</span>
    </div>
  </section>
  <section class="sign sign--white">
    <p class="sign__line sign__line--top">FOR</p>
    <p class="sign__line sign__line--bottom">SALE</p>
    <div class="brand">
      <span class="brand__mark"></span>
      <span class="brand__name">Maple Lane<br>Home Tour</span>
    </div>
  </section>
</main>
</body>
</html>
```